Business Card and Letterhead for Vantel Psychology

We need a business card design and letterhead to use for our Psychology firm that specializes in psychoeducational assessments and individual therapy. Our motto is Purpose-Driven Assessments, Meaning-Centered Therapy.Our contact information is as follows:
Vantel Psychology
The Bramwick Block - 4127-38St.
Box 6154 Brenton, MB
T2K 3R8
t 403.555.0148 (VANT)
f 403.555.0193
www.vantelpsych-example.ca
The business card will be used for two different psychologists so I can supply names nearer to completion. We prefer clean, uncluttered looks.

Target Market(s)

Clients, Educators

Font styles to use
Sans Serif

Colors

Designer to choose colors to be used in the design.

Requirements
Must have
• All relevant contact info, logo, some "white" space.
Nice to have
• It would be nice to see letterhead options that have the logo on the top of the page but also options that have it on the side. I think top of the page is probably our preference.
Should not have
• Too much clutter!

```html
<!DOCTYPE html>
<html lang="en">
<head>
<meta charset="utf-8">
<title>Vantel Psychology Stationery</title>
<link href="https://fonts.googleapis.com/css2?family=Open+Sans:wght@400;600;700&display=swap" rel="stylesheet">
<style>
  :root {
    --orange: #f4aa4b;
    --blue: #4fb9dc;
    --paper: #f3f3f3;
    --card-light: #ececec;
    --ink: #333333;
    --muted: #555555;
    --white: #ffffff;
  }
  * { margin: 0; padding: 0; box-sizing: border-box; }
  html, body { width: 1200px; height: 1015px; overflow: hidden; background: var(--white); }
  body { position: relative; font-family: "Open Sans", Arial, sans-serif; color: var(--ink); }

  .sheet { position: absolute; box-shadow: 4px 5px 10px rgba(0,0,0,.35); overflow: hidden; }
  .sheet svg.backdrop { position: absolute; inset: 0; }

  /* Letterhead */
  .letterhead { left: 94px; top: 161px; width: 539px; height: 695px; }
  .brand-mark { position: absolute; border-radius: 50%; }
  .letterhead .brand-mark { left: 404px; top: 42px; width: 36px; height: 36px; background: var(--blue); }
  .brand-name { position: absolute; font-weight: 700; letter-spacing: .04em; text-transform: uppercase; white-space: nowrap; }
  .letterhead .brand-name { left: 331px; top: 85px; width: 166px; text-align: center; font-size: 11px; color: var(--blue); }

  .letter-body { position: absolute; left: 122px; top: 192px; width: 350px; font-size: 9px; line-height: 12.4px; color: var(--ink); }
  .letter-body p { text-indent: 9px; margin-bottom: 7px; }

  .signature { position: absolute; right: 66px; top: 560px; font-size: 11px; color: var(--muted); letter-spacing: .02em; }

  .contact-list { position: absolute; left: 284px; top: 596px; list-style: none; font-size: 14.5px; line-height: 17px; color: var(--ink); }
  .contact-list li { display: flex; align-items: center; gap: 7px; }
  .contact-list svg { width: 10px; height: 10px; fill: var(--orange); flex: none; }

  /* Business cards */
  .card { width: 323px; height: 203px; }
  .card-front { left: 716px; top: 161px; background: var(--orange); }
  .card-front .brand-mark { left: 139px; top: 67px; width: 44px; height: 44px; background: var(--white); }
  .card-front .brand-name { left: 0; top: 126px; width: 323px; text-align: center; font-size: 17px; color: var(--white); }

  .card-back { left: 717px; top: 462px; }
  .card-back .brand-name { left: 22px; top: 27px; font-size: 11px; color: var(--blue); }
  .card-back .brand-mark { left: 228px; top: 100px; width: 44px; height: 44px; background: var(--blue); }
  .person-name { position: absolute; left: 22px; top: 63px; font-size: 12px; font-weight: 600; color: var(--white); text-transform: uppercase; }
  .person-name .first { color: var(--blue); }
  .person-role { position: absolute; left: 22px; top: 79px; font-size: 8px; color: var(--white); }
  .card-contacts { position: absolute; left: 22px; top: 115px; list-style: none; font-size: 8px; line-height: 11px; color: var(--white); }
  .card-contacts li { display: flex; align-items: center; gap: 4px; }
  .card-contacts svg { width: 6px; height: 6px; fill: var(--blue); }
  .card-address { position: absolute; left: 22px; top: 160px; font-size: 8px; line-height: 11px; color: var(--white); font-style: normal; }
</style>
</head>
<body>

<section class="sheet letterhead" aria-label="Letterhead">
  <svg class="backdrop" width="539" height="695" viewBox="0 0 539 695" aria-hidden="true">
    <rect width="539" height="695" fill="var(--orange)"/>
    <path d="M140,0 Q-30,350 140,695 L539,695 L539,0 Z" fill="var(--blue)"/>
    <path d="M164,0 Q-8,350 158,695 L539,695 L539,0 Z" fill="var(--paper)"/>
  </svg>
  <span class="brand-mark"></span>
  <span class="brand-name">Vantel Psychology</span>

  <div class="letter-body">
    <p>Lorem ipsum ad his scripta blandit partiendo, eum fastidii accumsan euripidis in, eum liber hendrerit an. Qui ut wisi vocibus suscipiantur, quo dicit ridens inciderint id. Quo mundi lobortis reformidans eu, legimus senserit definiebas an eos. Eu sit tincidunt incorrupte definitionem, vis mutat affert percipit cu, eirmod consectetuer.</p>
    <p>Lorem ipsum ad his scripta blandit partiendo, eum fastidii accumsan euripidis in, eum liber hendrerit an. Qui ut wisi vocibus suscipiantur, quo dicit ridens inciderint id. Quo mundi lobortis reformidans eu, legimus senserit definiebas an eos. Eu sit tincidunt incorrupte definitionem, vis mutat affert percipit cu, eirmod consectetuer signiferumque eu per. In usu latine equidem dolores. Quo no falli viris intellegam, ut fugit veritus placerat per.Lorem ipsum ad his scripta blandit partiendo, eum fastidii accumsan euripidis in, eum liber hendrerit an. Qui ut wisi vocibus suscipiantur, quo dicit ridens inciderint id. Quo mundi lobortis reformidans eu, legimus senserit definiebas an eos. Eu sit tincidunt incorrupte definitionem, vis mutat affert percipit cu, eirmod consectetuer.</p>
    <p>Lorem ipsum ad his scripta blandit partiendo, eum fastidii accumsan euripidis in, eum liber hendrerit an. Qui ut wisi vocibus suscipiantur, quo dicit ridens inciderint id. Quo mundi lobortis reformidans eu, legimus senserit definiebas an eos. Eu sit tincidunt incorrupte definitionem, vis mutat affert percipit cu, eirmod consectetuer.</p>
    <p>Lorem ipsum ad his scripta blandit partiendo, eum fastidii accumsan euripidis in, eum liber hendrerit an.</p>
  </div>

  <div class="signature">LOREM IPSUM</div>

  <ul class="contact-list">
    <li><svg viewBox="0 0 10 10"><path d="M2,0 L4,2.5 L3,3.8 Q4.5,6 6.2,7 L7.5,6 L10,8 L8.5,10 Q3,9 0,2 Z"/></svg>403.555.0148 (VANT)</li>
    <li><svg viewBox="0 0 10 10"><rect x="0" y="2" width="10" height="7" rx="1"/></svg>403.555.0193</li>
    <li><svg viewBox="0 0 10 10"><circle cx="5" cy="5" r="5"/></svg>www.vantelpsych-example.ca</li>
  </ul>
</section>

<section class="sheet card card-front" aria-label="Business card front">
  <span class="brand-mark"></span>
  <span class="brand-name">Vantel Psychology</span>
</section>

<section class="sheet card card-back" aria-label="Business card back">
  <svg class="backdrop" width="323" height="203" viewBox="0 0 323 203" aria-hidden="true">
    <rect width="323" height="203" fill="var(--orange)"/>
    <path d="M220,0 Q148,100 218,203 L323,203 L323,0 Z" fill="var(--blue)"/>
    <path d="M234,0 Q164,104 232,203 L323,203 L323,0 Z" fill="var(--card-light)"/>
  </svg>
  <span class="brand-name">Vantel Psychology</span>
  <div class="person-name"><span class="first">Lorem</span> Ipsham</div>
  <div class="person-role">psychologist</div>
  <ul class="card-contacts">
    <li><svg viewBox="0 0 10 10"><path d="M2,0 L4,2.5 L3,3.8 Q4.5,6 6.2,7 L7.5,6 L10,8 L8.5,10 Q3,9 0,2 Z"/></svg>403.555.0148 (VANT)</li>
    <li><svg viewBox="0 0 10 10"><rect x="0" y="2" width="10" height="7" rx="1"/></svg>403.555.0193</li>
    <li><svg viewBox="0 0 10 10"><circle cx="5" cy="5" r="5"/></svg>www.vantelpsych-example.ca</li>
  </ul>
  <address class="card-address">The Bramwick Block - 4127-38St.<br>Box 6154 Brenton, MB T2K 3R8</address>
  <span class="brand-mark"></span>
</section>

</body>
</html>
```